Vantor Burnished Concrete & Grinding
I'm looking for a business card and logo design for my
new Polished Concrete & Grinding business,
If you were to look up Vantor in the dictionary it would
say, first in importance, order, or position; leading.
Polished Concrete floors are a niche market, that are being used currently in Shopping centres, office spaces and by most high end architects, builders and designers.
i need my business card & logo to stand out from my
competitors, i need my design + logo to reflect this it
needs to be simple, professional, eye catching, easy
to read and scream quality. The logo will need to be
suitable for a whole range of applications including,
uniforms, letter heads, stickers, and eventually
incorporating in vehicle vinyl wrapping.
Target Market(s)
Builders, architects, Interior designers & home owners
Contact Information for Business Card
Front side:
- Vantor Burnished Concrete & Grinding.
- Logo
Rear side:
- Liam Verhorst
- 0481736502
- info@vantorbcg.com.au
- commercial - domestic - industrial
- (later down the line website & space for
social media links
www.vantorburnishedconcrete.com.au)
Colors
Designer to choose colors to be used in the design.
Look and feel

```html
<!DOCTYPE html>
<html lang="en">
<head>
<meta charset="utf-8">
<title>Vantor Burnished Concrete &amp; Grinding – Business Card</title>
<link rel="stylesheet" href="https://fonts.googleapis.com/css2?family=Montserrat:wght@700&family=Roboto:wght@400;500&display=swap">
<style>
  :root {
    --stage: #1d1e21;
    --card: #6c7278;
    --ink: #141517;
    --light: #d9dcdf;
    --rule: #c9ccd0;
  }
  * { box-sizing: border-box; margin: 0; padding: 0; }
  html, body { width: 1200px; height: 800px; overflow: hidden; background: var(--stage); }
  .canvas {
    width: 1200px; height: 800px;
    display: flex; align-items: center; justify-content: center; gap: 60px;
  }
  .card {
    position: relative;
    width: 525px; height: 300px;
    background: var(--card);
    border-radius: 3px;
    box-shadow: 0 18px 40px rgba(0,0,0,.55);
  }
  .brand {
    position: absolute;
    display: flex; align-items: center; gap: 12px;
    font-family: "Montserrat", sans-serif;
    font-weight: 700;
    color: var(--ink);
  }
  .brand-mark { width: 34px; height: 34px; background: var(--ink); flex: none; }
  .brand-name { line-height: 1.05; }
  .brand-name .line-1 { display: block; font-size: 30px; }
  .brand-name .line-2 { display: block; font-size: 13px; letter-spacing: 4.6px; margin-top: 4px; }

  .card-front .brand { left: 50%; top: 50%; transform: translate(-50%, -50%); }

  .card-back .brand { right: 34px; top: 54px; }
  .card-back .brand-name .line-1 { font-size: 26px; }
  .card-back .brand-name .line-2 { font-size: 11px; letter-spacing: 4px; }

  .holder {
    position: absolute; left: 30px; top: 182px;
    font-family: "Montserrat", sans-serif; font-weight: 700;
    font-size: 15px; color: var(--ink);
  }
  .sectors {
    position: absolute; right: 30px; top: 186px;
    font-family: "Roboto", sans-serif; font-size: 11px; color: var(--ink);
  }
  .divider {
    position: absolute; left: 30px; right: 30px; top: 208px;
    height: 1px; background: var(--rule);
  }
  .contact {
    position: absolute; left: 30px; top: 218px;
    list-style: none;
    font-family: "Roboto", sans-serif; font-size: 11.5px; color: var(--ink);
  }
  .contact li { display: flex; align-items: center; gap: 8px; height: 20px; }
  .contact svg { width: 12px; height: 12px; flex: none; }
  .social {
    position: absolute; right: 30px; top: 222px;
    display: flex; gap: 6px; list-style: none;
  }
  .social li {
    width: 18px; height: 18px; border-radius: 50%;
    border: 1.5px solid var(--light);
  }
</style>
</head>
<body>
<main class="canvas">
  <section class="card card-front" aria-label="Card front">
    <div class="brand">
      <span class="brand-mark"></span>
      <span class="brand-name"><span class="line-1">Vantor Burnished</span><span class="line-2">Concrete &amp; Grinding</span></span>
    </div>
  </section>

  <section class="card card-back" aria-label="Card back">
    <div class="brand">
      <span class="brand-mark"></span>
      <span class="brand-name"><span class="line-1">Vantor Burnished</span><span class="line-2">Concrete &amp; Grinding</span></span>
    </div>
    <p class="holder">Liam Verhorst</p>
    <p class="sectors">Commercial | Domestic | Industrial</p>
    <div class="divider"></div>
    <ul class="contact">
      <li>
        <svg viewBox="0 0 12 12" aria-hidden="true"><rect x="3" y="0.5" width="6" height="11" rx="1" fill="none" stroke="#e4e6e8" stroke-width="1.2"/></svg>
        0481736502
      </li>
      <li>
        <svg viewBox="0 0 12 12" aria-hidden="true"><rect x="0.6" y="2" width="10.8" height="8" fill="none" stroke="#e4e6e8" stroke-width="1.2"/><path d="M0.6 2 L6 6.5 L11.4 2" fill="none" stroke="#e4e6e8" stroke-width="1.2"/></svg>
        info@vantorbcg.com.au
      </li>
      <li>
        <svg viewBox="0 0 12 12" aria-hidden="true"><circle cx="6" cy="6" r="5.2" fill="none" stroke="#e4e6e8" stroke-width="1.2"/><path d="M0.8 6 H11.2 M6 0.8 C3 4 3 8 6 11.2 M6 0.8 C9 4 9 8 6 11.2" fill="none" stroke="#e4e6e8" stroke-width="1"/></svg>
        www.vantorburnishedconcrete.com.au
      </li>
    </ul>
    <ul class="social" aria-label="Social media links">
      <li></li><li></li><li></li><li></li><li></li>
    </ul>
  </section>
</main>
</body>
</html>
```